ZorvaĀ®? Cartridge Box

Zorva is a new, patent pending nebulizer-like technology. It comes with disposable, 12 ml cartridges. We are wanting an design an outer, retail box for the cartridge. The box is white, its size is a 35mm x 35mm x 90mm, the typical size for a 30 ml boston Round tincture bottle.

```html
<!DOCTYPE html>
<html lang="en">
<head>
<meta charset="utf-8">
<title>Zorva® Cartridge Box – Dieline</title>
<link href="https://fonts.googleapis.com/css2?family=Kurale&family=Vollkorn:ital,wght@0,400;1,400&family=Roboto:wght@400;700&display=swap" rel="stylesheet">
<style>
  :root {
    --backdrop: #d4d4d4;
    --board: #f1f1ef;
    --board-edge: #dcdcda;
    --fold: #e2e2e0;
    --ink: #2e2e2e;
    --accent: #36d2ec;
  }
  * { margin: 0; padding: 0; box-sizing: border-box; }
  html, body {
    width: 1200px; height: 853px; overflow: hidden;
    background: var(--backdrop);
  }
  .canvas { position: relative; width: 1200px; height: 853px; }
  .dieline { position: absolute; inset: 0; }
  .dieline .board { fill: var(--board); stroke: var(--board-edge); stroke-width: 0.8; }
  .dieline .fold { stroke: var(--fold); stroke-width: 0.8; fill: none; }

  .face {
    position: absolute;
    display: flex; flex-direction: column; align-items: center;
    color: var(--ink);
  }
  .face--front { left: 436px; top: 257px; width: 117px; }
  .face--back  { left: 668px; top: 251px; width: 120px; }

  .brand {
    display: flex; align-items: center; gap: 6px;
    margin-top: 68px; height: 24px;
    font-family: "Roboto", sans-serif; font-weight: 700;
    font-size: 23px; line-height: 1; color: var(--ink);
  }
  .brand__dot { width: 13px; height: 13px; border-radius: 50%; background: var(--accent); }

  .product {
    margin-top: 58px; height: 20px;
    font-family: "Vollkorn", serif; font-weight: 400;
    font-size: 16px; line-height: 20px; color: var(--ink);
  }

  .blend {
    margin-top: 58px;
    font-family: "Vollkorn", serif; font-style: italic;
    font-size: 11.5px; line-height: 14px; text-align: center;
  }
  .claim {
    margin-top: 55px;
    font-family: "Roboto", sans-serif; font-size: 7px; line-height: 9px; text-align: center;
  }
  .volume-band {
    margin-top: 8px; width: 100%; height: 15px;
    background: var(--accent);
    font-family: "Kurale", serif; font-size: 9.5px; line-height: 15px;
    text-align: center; color: var(--ink);
  }
</style>
</head>
<body>
<main class="canvas">
  <svg class="dieline" width="1200" height="853" viewBox="0 0 1200 853" aria-hidden="true">
    <rect class="board" x="317" y="257" width="471" height="355"/>
    <path class="board" d="M788 256 L822 266 L828 597 L788 611 Z"/>
    <path class="board" d="M317 257 L317 251 L328 243 L332 200 Q334 185 349 185 L426 184 L427 251 L436 257 Z"/>
    <path class="board" d="M436 257 L434 135 Q434 115 455 115 L532 114 Q552 114 552 135 L553 257 Z"/>
    <line class="fold" x1="435" y1="140" x2="552" y2="139"/>
    <path class="board" d="M553 257 L553 245 L560 200 Q562 183 578 183 L650 183 L660 240 L668 247 L668 257 Z"/>
    <path class="board" d="M321 612 L321 618 L331 626 L334 688 L408 688 Q425 688 428 675 L432 638 L441 630 L441 612 Z"/>
    <path class="board" d="M553 612 L553 625 L562 633 L567 672 Q569 685 582 685 L660 684 L662 623 L668 612 Z"/>
    <path class="board" d="M670 611 L674 740 Q675 757 692 757 L774 756 Q790 756 790 740 L788 611 Z"/>
    <line class="fold" x1="674" y1="740" x2="790" y2="740"/>
    <line class="fold" x1="436" y1="257" x2="436" y2="612"/>
    <line class="fold" x1="553" y1="257" x2="553" y2="612"/>
    <line class="fold" x1="668" y1="257" x2="668" y2="612"/>
    <line class="fold" x1="788" y1="257" x2="788" y2="611"/>
  </svg>

  <section class="face face--front">
    <div class="brand"><span class="brand__dot"></span>Zorva®</div>
    <div class="product">Velmora</div>
    <p class="blend">Anti<br>Nausea Blend</p>
    <p class="claim">Patent Pending<br>Nebulizer</p>
    <div class="volume-band">12 ml cartridges</div>
  </section>

  <section class="face face--back">
    <div class="brand"><span class="brand__dot"></span>Zorva®</div>
    <div class="product">Velmora</div>
    <p class="blend">Anti<br>Nausea Blend</p>
    <p class="claim">Patent Pending<br>Nebulizer</p>
    <div class="volume-band">12 ml cartridges</div>
  </section>
</main>
</body>
</html>
```